Elder abuse Infographic Poster for doctor surgeries

I am looking for someone to redesign, or clean up an infographic poster that we have drafted to raise awareness for Elder abuse. The colour for elder abuse is deep dark purple, and we would like it to be high resolution so it can be printed A3 size and placed in Doctor surgeries. The poster will be used by a not-for-profit in Australia. We are looking to use pictures, rather than heavy text blocks, following the Infographic poster style (I have included a couple of infographic posters for inspiration).
Reason: Providing extra time for more designs :)
Target Market(s)
Older people, 60+
Industry/Entity Type
Doctor
Requirements
Nice to have
- NOTE: You do not need to use the banner etc I have attached, its just an idea for the colours we use etc.
Should not have
- Images of frail older people, pastel colourings, or anything typically associated with frail aged.

```html
<!DOCTYPE html>
<html lang="en">
<head>
<meta charset="utf-8">
<title>There Is No Excuse For Elder Abuse</title>
<link rel="stylesheet" href="https://fonts.googleapis.com/css2?family=Anton&family=Arimo:wght@400;700&display=swap">
<style>
  :root {
    --night-purple: #221c4f;
    --alert-red: #ee2a3b;
    --panel-black: #000000;
    --paper-white: #ffffff;
    --brand-magenta: #c1348f;
    --display-font: "Anton", Impact, sans-serif;
    --body-font: "Arimo", Arial, sans-serif;
  }
  * { margin: 0; padding: 0; box-sizing: border-box; }
  html, body { width: 848px; height: 1200px; overflow: hidden; background: var(--night-purple); }
  .poster {
    position: relative;
    width: 848px;
    height: 1200px;
    background: var(--night-purple);
    font-family: var(--body-font);
    color: var(--paper-white);
  }
  .brand-tag {
    position: absolute;
    background: var(--paper-white);
    display: flex;
    align-items: center;
    justify-content: center;
    flex-direction: column;
  }
  .brand-tag .brand-name {
    font-family: var(--body-font);
    font-weight: 700;
    color: var(--brand-magenta);
    line-height: 1;
  }
  .brand-tag--top { left: 52px; top: 117px; width: 240px; height: 84px; }
  .brand-tag--top .brand-name { font-size: 34px; }
  .brand-tag--bottom { left: 567px; top: 1087px; width: 202px; height: 64px; }
  .brand-tag--bottom .brand-name { font-size: 28px; }

  .stop-sign { position: absolute; left: 300px; top: 40px; width: 244px; height: 238px; }
  .stop-sign__stat {
    position: absolute; left: 0; right: 0; top: 48px;
    text-align: center; font-size: 12px; line-height: 1.15; color: var(--paper-white);
  }
  .stop-sign__word {
    position: absolute; left: 0; right: 0; top: 78px;
    text-align: center; font-family: var(--body-font); font-size: 66px; line-height: 1;
    letter-spacing: 1px; color: var(--paper-white);
  }
  .headline {
    position: absolute; left: 544px; top: 56px;
    font-family: var(--display-font); font-size: 47px; line-height: 1.0;
    text-transform: uppercase; color: var(--paper-white); letter-spacing: 0.5px;
  }
  .divider { position: absolute; left: 42px; width: 758px; height: 10px; background: var(--panel-black); }
  .divider--upper { top: 287px; }
  .divider--lower { top: 973px; }

  .info-panel {
    position: absolute; width: 368px; background: var(--panel-black);
    padding-top: 14px; text-align: center;
  }
  .info-panel--risk { left: 42px; top: 312px; height: 316px; }
  .info-panel--prevention { left: 432px; top: 312px; height: 316px; }
  .info-panel--types { left: 42px; top: 636px; height: 317px; }
  .info-panel--stopping { left: 432px; top: 636px; height: 317px; }
  .info-panel__title {
    font-family: var(--display-font); font-weight: 400; font-size: 35px; line-height: 1;
    color: var(--alert-red); letter-spacing: 0.5px; margin-bottom: 6px;
  }
  .info-panel__list { list-style: none; font-size: 20px; line-height: 0.92; text-transform: uppercase; }
  .info-panel__list li { margin-bottom: 18px; }
  .info-panel--risk .info-panel__list li { margin-bottom: 17px; line-height: 1; }
  .info-panel__list--detail {
    text-align: left; font-size: 15px; line-height: 1.3; text-transform: none;
    padding-left: 5px; margin-top: 10px;
  }
  .info-panel__list--detail li { margin-bottom: 20px; }
  .info-panel__list--detail .indent { padding-left: 100px; display: block; }

  .helpline {
    position: absolute; left: 0; width: 842px; top: 998px; text-align: center;
    font-family: var(--display-font); font-size: 43px; line-height: 1; color: var(--alert-red);
    letter-spacing: 0.5px;
  }
  .helpline__note {
    position: absolute; left: 0; width: 842px; top: 1056px; text-align: center;
    font-size: 20px; letter-spacing: 0.3px; color: var(--paper-white);
  }
</style>
</head>
<body>
<main class="poster">
  <div class="brand-tag brand-tag--top"><span class="brand-name">Kinwell</span></div>

  <div class="stop-sign">
    <svg width="244" height="238" viewBox="0 0 244 238" aria-hidden="true">
      <polygon points="72,0 172,0 244,70 244,168 172,238 72,238 0,168 0,70" fill="var(--alert-red)"/>
    </svg>
    <p class="stop-sign__stat">1 in 20 older people will<br>experience elder abuse</p>
    <p class="stop-sign__word">STOP</p>
    <svg style="position:absolute;left:58px;top:150px" width="128" height="46" viewBox="0 0 128 46" role="img" aria-label="Row of twenty small figures, one highlighted, showing 1 in 20">
      <rect x="0" y="0" width="128" height="46" fill="#f6b3b9"/>
    </svg>
  </div>

  <h1 class="headline">There is<br>no excuse<br>for<br>elder abuse</h1>

  <div class="divider divider--upper"></div>

  <section class="info-panel info-panel--risk">
    <h2 class="info-panel__title">RISK FACTORS</h2>
    <ul class="info-panel__list">
      <li>Illness</li>
      <li>Difficulty managing money</li>
      <li>Independence</li>
      <li>Isolation</li>
    </ul>
  </section>

  <section class="info-panel info-panel--prevention">
    <h2 class="info-panel__title">PREVENTION</h2>
    <ul class="info-panel__list">
      <li>Stay connected to<br>friends,<br>family and community</li>
      <li>Know your rights</li>
      <li>Access professional<br>services to prevent<br>family dependence</li>
      <li>Consult a lawyer<br>before signing<br>agreements</li>
    </ul>
  </section>

  <section class="info-panel info-panel--types">
    <h2 class="info-panel__title">TYPES OF ABUSE</h2>
    <ul class="info-panel__list info-panel__list--detail">
      <li>PSYCHOLOGICAL (bullying shouting,swearing)</li>
      <li>SOCIAL (stopping access to family/friends)</li>
      <li>FINANCIAL (taking money, not allowing access<span class="indent">to accounts)</span></li>
      <li>NEGLECT (withholding essential care)</li>
      <li>SEXUAL(inappropriate touching</li>
      <li>PHYSICAL (hitting, slapping and physical harm)</li>
    </ul>
  </section>

  <section class="info-panel info-panel--stopping">
    <h2 class="info-panel__title">STOPPING ABUSE</h2>
    <ul class="info-panel__list">
      <li>Speak to a health<br>professional</li>
      <li>Contact an advocate</li>
      <li>Consult a lawyer</li>
    </ul>
  </section>

  <div class="divider divider--lower"></div>

  <p class="helpline">ELDER ABUSE HELPLINE&nbsp; 1300 555 018</p>
  <p class="helpline__note">FREE, INDEPENDENT, CLIENT FOCUSED AND CONFIDENTIAL</p>

  <div class="brand-tag brand-tag--bottom"><span class="brand-name">Kinwell</span></div>
</main>
</body>
</html>
```